Need a modern, bold, luxurious advertisement flyer for our roofing company. located in buffalo, ny. Big house with a intense roof design asphalt shingles. slogan is "Reliability starts at the top". Colors varies but want it to be modern. we will be handing these out when we are working in the area. phone number is 716-555-0143 for the TRUE PEAK estimate. also our services are roofing, roof repairs, gutters, attic ventilation. we offer a 15 year warranty with our summit shield plan. We are certified by dwellmatch, harlan pike, skarn. Also follow us on facebook, google and yelp. website is tpk-roofing.example, facebook is tpkroofing. pictures are on facebook and our website if need more can be provided. also can include a review we have.

```html
<!DOCTYPE html>
<html lang="en">
<head>
<meta charset="UTF-8">
<title>TRUE PEAK Roofing Flyer</title>
<link href="https://fonts.googleapis.com/css2?family=Barlow+Semi+Condensed:wght@500;600;700;800&family=Saira:wght@400&display=swap" rel="stylesheet">
<style>
  :root {
    --orange: #e8911f;
    --orange-deep: #d97c14;
    --charcoal: #3a3a3c;
    --cream: #f3eee4;
    --ink: #2f2f31;
    --white: #ffffff;
    --stage: #e7e4df;
  }
  * { margin: 0; padding: 0; box-sizing: border-box; }
  html, body { width: 1188px; height: 1200px; overflow: hidden; }
  body {
    background: var(--stage);
    font-family: "Barlow Semi Condensed", "Arial Narrow", sans-serif;
    position: relative;
  }
  .flyer {
    position: absolute;
    left: 181px; top: 16px;
    width: 826px; height: 1168px;
    background: var(--charcoal);
    overflow: hidden;
  }
  .hero-photo {
    position: absolute; left: 0; top: 0; width: 826px; height: 540px;
    background:
      linear-gradient(180deg, #b9bcc0 0%, #8d7f7a 45%, #6e5a55 70%, #5a3f3a 78%, #c79656 80%, #b9823f 100%);
  }
  .brand-column {
    position: absolute; left: 440px; top: 0; width: 370px; height: 548px;
    background: rgba(232, 145, 31, 0.88);
  }
  .logo-panel {
    position: absolute; left: 458px; top: 10px; width: 340px; height: 258px;
    background: var(--cream);
    clip-path: polygon(0 0, 100% 0, 100% 78%, 50% 100%, 0 78%);
    text-align: center;
  }
  .brand-name {
    margin-top: 92px;
    font-weight: 800;
    font-size: 54px;
    letter-spacing: 2px;
    color: var(--orange);
    line-height: 1;
  }
  .brand-tagline {
    margin-top: 12px;
    font-family: "Saira", sans-serif;
    font-size: 18px;
    letter-spacing: 0.5px;
    color: var(--orange-deep);
  }
  .headline {
    position: absolute; left: 445px; top: 296px; width: 365px;
    text-align: center;
    color: var(--white);
    font-weight: 800;
    font-size: 60px;
    line-height: 1.1;
    text-transform: uppercase;
  }
  .gallery {
    position: absolute; left: 36px; top: 508px; width: 760px; height: 170px;
    display: flex; justify-content: space-between;
  }
  .gallery-photo {
    width: 238px; height: 168px;
    border: 5px solid var(--white);
  }
  .gallery-photo.framing { background: linear-gradient(160deg, #e4e6e8 0%, #b0764a 45%, #8b6a52 100%); }
  .gallery-photo.underlay { background: linear-gradient(135deg, #6b5a4e 0%, #8c7566 45%, #e6d5d2 55%, #f0c9c9 100%); }
  .gallery-photo.house { background: linear-gradient(180deg, #bfcbd6 0%, #7a5a44 45%, #5c4434 70%, #8a8884 100%); }
  .services {
    position: absolute; left: 36px; top: 696px; width: 760px;
    text-align: center; color: var(--orange);
  }
  .services-title {
    display: flex; align-items: center; justify-content: center; gap: 16px;
    font-weight: 700; font-size: 33px; text-transform: uppercase;
  }
  .services-title::before, .services-title::after {
    content: ""; width: 225px; height: 3px; background: var(--orange);
  }
  .services-list {
    margin-top: 6px;
    font-weight: 600; font-size: 22px; line-height: 31px; text-transform: uppercase;
  }
  .certified { color: var(--white); font-weight: 600; font-size: 19px; line-height: 31px; text-transform: uppercase; }
  .crew-photo {
    position: absolute; left: 0; top: 826px; width: 470px; height: 342px;
    background: linear-gradient(120deg, #9fb2c4 0%, #d9d6cd 35%, #9a9a98 60%, #c7c4bb 100%);
  }
  .warranty {
    position: absolute; left: 470px; top: 826px; width: 356px; height: 342px;
    background: var(--white);
  }
  .warranty-text {
    position: absolute; left: 0; top: 52px; width: 356px;
    text-align: center; text-transform: uppercase;
    color: var(--ink); font-weight: 700; font-size: 24px; line-height: 34px;
  }
  .warranty-text .accent { color: var(--orange); font-size: 31px; }
  .contact {
    position: absolute; left: 470px; top: 1022px; width: 356px; height: 118px;
    background: var(--orange);
    color: var(--white); text-align: center;
    font-weight: 700; font-size: 34px; line-height: 40px;
    padding-top: 18px; text-transform: uppercase;
  }
  .contact .web { font-size: 31px; }
  .social {
    position: absolute; left: 470px; top: 1140px; width: 356px; height: 28px;
    text-align: center; color: var(--ink);
    font-weight: 600; font-size: 16px; line-height: 28px; text-transform: uppercase;
  }
</style>
</head>
<body>
  <main class="flyer">
    <div class="hero-photo" role="img" aria-label="Roofer in work gloves laying asphalt shingles on a roof"></div>
    <div class="brand-column"></div>
    <div class="logo-panel">
      <div class="brand-name">TRUE PEAK</div>
      <div class="brand-tagline">ROOFING-SIDING-STONE</div>
    </div>
    <h1 class="headline">Reliability<br>starts at<br>the top</h1>

    <section class="gallery">
      <div class="gallery-photo framing" role="img" aria-label="Crew working on exposed roof framing in winter"></div>
      <div class="gallery-photo underlay" role="img" aria-label="Roof with shingles and underlayment partly installed"></div>
      <div class="gallery-photo house" role="img" aria-label="House with ladders and trailer during a roof job"></div>
    </section>

    <section class="services">
      <h2 class="services-title">Services</h2>
      <p class="services-list">• Roofing • Roof repairs • Gutters • Attic ventilation</p>
      <p class="certified">Certified by dwellmatch • harlan pike • skarn</p>
    </section>

    <div class="crew-photo" role="img" aria-label="Worker installing a gutter on a sided house"></div>
    <section class="warranty">
      <p class="warranty-text">We offer a<br><span class="accent">15 year warranty</span><br>with our summit<br>shield plan</p>
    </section>
    <section class="contact">
      <div class="phone">716-555-0143</div>
      <div class="web">tpk-roofing.example</div>
    </section>
    <p class="social">Follow us online: tpkroofing</p>
  </main>
</body>
</html>
```